Blue Harbor Audio

need a business card for a dj and sound equipment hire(rentals) business based in Melbourne. i have attached a current card get an idea. card needs to be unique professional looking.

ps.this card is not for a DJ. it's a rental business of dj equipment and pa systems.

Industry/Entity Type

Business

Font styles to use
Sans Serif
Script

Requirements
Must have
• Business Name: BLUE HARBOR AUDIO
Contact Person: RAVINDU PERERA
Mobile: 047 BLAST 28
Email: RAVINDU@BLUEHARBORAUDIO.COM.AU
Website: WWW.BLUEHARBORAUDIO.COM.AU
Facebook: WWW.FANPAGE.CM/BLUEHARBORAUDIO.COM.AU

```html
<!DOCTYPE html>
<html lang="en">
<head>
<meta charset="utf-8">
<title>Blue Harbor Audio – Business Card</title>
<link href="https://fonts.googleapis.com/css2?family=Open+Sans:ital,wght@0,400;0,600;0,700;0,800;1,400&display=swap" rel="stylesheet">
<style>
  :root {
    --teal: #1f7a8c;
    --mist: #b5c5cc;
    --ink: #0a0a0a;
    --paper: #ffffff;
    --photo-dark: #2a2723;
    --photo-mid: #6b655d;
    --photo-light: #a8a29a;
  }
  * { margin: 0; padding: 0; box-sizing: border-box; }
  html, body { width: 1200px; height: 741px; overflow: hidden; background: var(--paper); }
  body { font-family: "Open Sans", sans-serif; color: var(--ink); }

  .card { position: relative; width: 1200px; height: 741px; background: var(--paper); overflow: hidden; }

  .accent-ring { position: absolute; left: 649px; top: 145px; width: 480px; height: 480px; border-radius: 50%; background: var(--mist); }

  .hero-photo {
    position: absolute; left: 0; top: 0; width: 1200px; height: 483px;
    background:
      radial-gradient(ellipse at 30% 20%, var(--photo-light) 0%, transparent 45%),
      linear-gradient(160deg, var(--photo-mid) 0%, var(--photo-dark) 70%);
  }

  .brand-disc {
    position: absolute; left: 632px; top: 32px; width: 514px; height: 514px;
    border-radius: 50%; background: var(--paper);
    display: flex; flex-direction: column; align-items: center; justify-content: center;
    text-align: center;
  }
  .brand-name {
    font-weight: 800; color: var(--teal);
    font-size: 58px; line-height: 1.02; letter-spacing: -0.5px;
  }
  .brand-tagline {
    margin-top: 10px; font-style: italic; font-size: 27px; color: #1a1a1a;
  }

  .contact-person { position: absolute; left: 145px; top: 535px; }
  .contact-name { font-weight: 700; font-size: 46px; line-height: 1; letter-spacing: 0.5px; }
  .contact-mobile { margin-top: 10px; font-weight: 700; font-size: 33px; line-height: 1; letter-spacing: 0.5px; }

  .contact-links {
    position: absolute; left: 16px; top: 676px; right: 10px;
    list-style: none;
    display: flex; gap: 14px; align-items: center;
  }
  .contact-link { display: flex; align-items: center; gap: 7px; font-size: 19px; white-space: nowrap; }
  .link-dot { width: 41px; height: 41px; border: 3px solid var(--teal); border-radius: 50%; flex: none; }
</style>
</head>
<body>
  <main class="card">
    <div class="accent-ring"></div>
    <div class="hero-photo" role="img" aria-label="Close-up photograph of a microphone resting on a sound mixing desk with rows of knobs"></div>

    <div class="brand-disc">
      <div class="brand-name">Blue Harbor<br>Audio</div>
      <div class="brand-tagline">sound equipment hire</div>
    </div>

    <section class="contact-person">
      <h1 class="contact-name">RAVINDU PERERA</h1>
      <p class="contact-mobile">047 BLAST 28</p>
    </section>

    <ul class="contact-links">
      <li class="contact-link"><span class="link-dot"></span>ravindu@blueharboraudio.com.au</li>
      <li class="contact-link"><span class="link-dot"></span>www.blueharboraudio.com.au</li>
      <li class="contact-link"><span class="link-dot"></span>www.fanpage.cm/blueharboraudio.com.au</li>
    </ul>
  </main>
</body>
</html>
```